Waterjet manufacturing company needs brochure design

We need a brochure that outlines why waterjet manufacturing is beneficial for a variety of industries, our capabilities, core competencies and competitive advantages (see attached documents). The design should include our logo and include the same colours. (Dark blue RGB – 2,86,162, Light Blue RGB – 0,146,201). The design should be very clean, professional and eye catching. I've attached a few photos that can be used. Regarding the photo of the robot, please make the background white.

Manufacturing, construction, aerospace, home building

• - exact Logo colours included in design (see description)
• - booklet style design (not tri-fold)
• - professional looking
• - Logo on front cover with writing underneath:
• High Quality
• Tight Tolerance
• Components
• - Plankrow, Ropelane, Vidstow and Pixelmorra icons in Contact Us section

```html
<!DOCTYPE html>
<html lang="en">
<head>
<meta charset="utf-8">
<title>Rivermark Waterjet Brochure</title>
<link rel="stylesheet" href="https://fonts.googleapis.com/css2?family=Montserrat:wght@400;600;700;800&family=Open+Sans:wght@400;600&display=swap">
<style>
:root{
  --navy:#0256a2;
  --sky:#0092c9;
  --deep:#013c75;
  --ink:#1d2733;
  --grey:#5b6571;
  --paper:#ffffff;
  --rule:#e3e8ee;
  --stage:#eef1f4;
}
*{box-sizing:border-box;margin:0;padding:0}
html,body{width:1200px;height:2556px;overflow:hidden;background:var(--stage)}
body{position:relative;font-family:"Open Sans",Arial,sans-serif;color:var(--ink)}
.spread{position:absolute;left:0;width:1200px;height:820px;background:var(--paper);overflow:hidden}
.spread-cover{top:0}
.spread-benefits{top:868px}
.spread-compare{top:1736px}
.fold{position:absolute;left:599px;top:0;width:2px;height:100%;background:linear-gradient(90deg,rgba(0,0,0,.08),rgba(0,0,0,0));z-index:5}
.layer{position:absolute;left:0;top:0}
.heading{font-family:"Montserrat",Arial,sans-serif;font-weight:800;line-height:1.05}
.heading .accent{color:var(--sky)}

/* Cover spread */
.contact-title{position:absolute;left:70px;top:140px;font-size:46px;color:var(--navy)}
.contact-sub{position:absolute;left:70px;top:200px;font-family:"Montserrat",Arial,sans-serif;font-weight:600;font-size:16px;color:var(--sky)}
.contact-list{position:absolute;left:70px;top:258px;list-style:none}
.contact-list li{display:flex;align-items:center;height:38px;font-size:14px;color:var(--grey)}
.contact-icon{width:28px;height:28px;border-radius:50%;background:var(--navy);margin-right:14px;display:flex;align-items:center;justify-content:center;flex:none}
.contact-icon.social{background:var(--sky)}
.brand{position:absolute;right:60px;top:60px;display:flex;align-items:center;gap:12px}
.brand-mark{width:34px;height:34px;background:var(--navy)}
.brand-name{font-family:"Montserrat",Arial,sans-serif;font-weight:800;font-size:24px;color:var(--navy);letter-spacing:.5px}
.tagline{position:absolute;right:60px;top:540px;text-align:right;font-size:64px;color:var(--navy)}

/* Benefits spread */
.why-title{position:absolute;left:60px;top:80px;font-size:32px;color:var(--ink)}
.why-body{position:absolute;left:60px;top:190px;width:330px;font-size:12.5px;line-height:1.7;color:var(--grey)}
.why-body p{margin-bottom:16px}
.benefits-head{position:absolute;left:670px;top:60px;width:480px;padding:18px 20px;background:var(--paper);border-radius:0 0 0 28px;text-align:center;font-family:"Montserrat",Arial,sans-serif;color:var(--navy)}
.benefits-head .small{font-size:16px;font-weight:600}
.benefits-head .big{font-size:19px;font-weight:800;color:var(--ink);white-space:nowrap}
.benefit-grid{position:absolute;left:650px;top:210px;width:510px;display:grid;grid-template-columns:repeat(4,1fr);row-gap:44px;column-gap:10px}
.benefit{text-align:center;color:#fff}
.benefit-icon{width:66px;height:66px;margin:0 auto 12px;border:2px solid #fff;border-radius:50%;display:flex;align-items:center;justify-content:center}
.benefit h3{font-family:"Montserrat",Arial,sans-serif;font-size:13px;font-weight:700;margin-bottom:6px}
.benefit p{font-size:10.5px;line-height:1.5;color:#d6e6f5}

/* Compare spread */
.compare-title{position:absolute;left:60px;top:70px;font-size:32px;color:var(--ink)}
.compare-table{position:absolute;left:60px;top:170px;width:500px;border-collapse:collapse;font-size:11.5px}
.compare-table th{background:var(--navy);color:#fff;font-family:"Montserrat",Arial,sans-serif;font-size:12px;text-align:left;padding:12px 10px}
.compare-table td{padding:14px 10px;border-bottom:1px solid var(--rule);color:var(--grey);vertical-align:top;height:64px}
.compare-table td:first-child{font-family:"Montserrat",Arial,sans-serif;font-weight:700;color:var(--navy);font-size:11px;text-transform:uppercase}
.compare-table tr:nth-child(even) td{background:#f4f7fa}
.materials-title{position:absolute;left:650px;top:70px;font-size:32px;color:var(--ink)}
.materials-grid{position:absolute;left:640px;top:170px;width:520px;height:600px;display:grid;grid-template-columns:repeat(4,1fr);grid-template-rows:1fr 1fr;gap:3px}
.material{padding:22px 12px;color:#fff;text-align:center;background:var(--navy)}
.material:nth-child(even){background:var(--deep)}
.material:nth-child(5),.material:nth-child(7){background:var(--deep)}
.material:nth-child(6),.material:nth-child(8){background:var(--navy)}
.material h3{font-family:"Montserrat",Arial,sans-serif;font-size:13px;font-weight:700;text-transform:uppercase;margin-bottom:12px;letter-spacing:.5px}
.material p{font-size:10.5px;line-height:1.6;color:#d6e6f5}
</style>
</head>
<body>

<!-- Cover spread -->
<section class="spread spread-cover">
  <h2 class="heading contact-title">Contact Us</h2>
  <p class="contact-sub">Not sure if we can help? Give us a call!</p>
  <ul class="contact-list">
    <li><span class="contact-icon"><svg width="14" height="14" viewBox="0 0 24 24"><path fill="#fff" d="M6.6 10.8a15 15 0 0 0 6.6 6.6l2.2-2.2a1 1 0 0 1 1-.25 11.4 11.4 0 0 0 3.6.57 1 1 0 0 1 1 1V20a1 1 0 0 1-1 1A17 17 0 0 1 3 4a1 1 0 0 1 1-1h3.5a1 1 0 0 1 1 1c0 1.25.2 2.45.57 3.6a1 1 0 0 1-.25 1z"/></svg></span>(555) 014-2290</li>
    <li><span class="contact-icon"><svg width="14" height="14" viewBox="0 0 24 24"><rect x="3" y="5" width="18" height="14" rx="2" fill="#fff"/><path d="M3 6l9 7 9-7" stroke="#0256a2" stroke-width="2" fill="none"/></svg></span>hello@rivermarkwaterjet.com</li>
    <li><span class="contact-icon"><svg width="14" height="14" viewBox="0 0 24 24"><circle cx="12" cy="12" r="9" stroke="#fff" stroke-width="2" fill="none"/><path d="M3 12h18M12 3c3 3 3 15 0 18M12 3c-3 3-3 15 0 18" stroke="#fff" stroke-width="1.6" fill="none"/></svg></span>www.rivermarkwaterjet.com</li>
    <li><span class="contact-icon"><svg width="14" height="14" viewBox="0 0 24 24"><path fill="#fff" d="M12 2a7 7 0 0 0-7 7c0 5 7 13 7 13s7-8 7-13a7 7 0 0 0-7-7zm0 9.5A2.5 2.5 0 1 1 12 6.5a2.5 2.5 0 0 1 0 5z"/></svg></span>48 Foundry Lane, Cedar Falls</li>
    <li><span class="contact-icon social"></span>Plankrow</li>
    <li><span class="contact-icon social"></span>Ropelane</li>
    <li><span class="contact-icon social"></span>Vidstow</li>
    <li><span class="contact-icon social"></span>Pixelmorra</li>
  </ul>

  <svg class="layer" width="1200" height="820" viewBox="0 0 1200 820" aria-hidden="true">
    <polygon points="330,420 460,720 330,720" fill="var(--navy)"/>
    <polygon points="860,110 960,110 840,410" fill="var(--sky)" opacity=".85"/>
    <polygon points="850,420 775,700 715,700" fill="var(--deep)"/>
    <line x1="470" y1="96" x2="900" y2="96" stroke="var(--sky)" stroke-width="3"/>
  </svg>
  <svg class="layer" style="left:360px;top:120px" width="540" height="580" viewBox="0 0 540 580" role="img" aria-label="Photograph of a waterjet cutting head working on a metal plate">
    <defs><linearGradient id="coverPhoto" x1="0" y1="0" x2="1" y2="1"><stop offset="0" stop-color="#9fb4c8"/><stop offset=".55" stop-color="#4e6a86"/><stop offset="1" stop-color="#24384f"/></linearGradient></defs>
    <polygon points="120,0 400,0 500,290 400,580 120,580 0,290" fill="url(#coverPhoto)"/>
  </svg>

  <div class="brand"><span class="brand-mark"></span><span class="brand-name">Rivermark Waterjet</span></div>
  <h1 class="heading tagline">We Make<br>The Cut!</h1>
  <div class="fold"></div>
</section>

<!-- Why choose / Benefits spread -->
<section class="spread spread-benefits">
  <svg class="layer" width="1200" height="820" viewBox="0 0 1200 820" aria-hidden="true">
    <polygon points="620,0 1200,0 1200,820 620,820 560,410" fill="var(--navy)"/>
    <polygon points="560,410 620,820 520,820" fill="var(--deep)"/>
  </svg>
  <svg class="layer" style="left:420px;top:110px" width="200" height="600" viewBox="0 0 200 600" role="img" aria-label="Photograph of precision cut metal parts">
    <defs><linearGradient id="whyPhoto" x1="0" y1="0" x2="0" y2="1"><stop offset="0" stop-color="#b8c7d6"/><stop offset="1" stop-color="#3f5a78"/></linearGradient></defs>
    <polygon points="0,0 140,0 190,300 140,600 0,600" fill="url(#whyPhoto)"/>
  </svg>

  <h2 class="heading why-title">Why Choose<br><span class="accent">Rivermark Waterjet</span></h2>
  <div class="why-body">
    <p>Rivermark Waterjet delivers precise parts for manufacturing, construction, aerospace and home building. Our team pairs modern cutting systems with practical shop experience, so every order arrives accurate, clean and ready for the next step of your project.</p>
    <p>Waterjet cutting shapes almost any material without heat, which keeps edges smooth and properties unchanged. We handle prototypes, short runs and full production jobs with the same care, tight tolerances and dependable turnaround you can plan around.</p>
    <p>From first drawing to final part, we work closely with your engineers to reduce waste, simplify finishing and keep costs under control. Talk to us about your next job and see how clean cutting can move your work forward.</p>
  </div>

  <div class="benefits-head"><div class="small">Benefits of</div><div class="big">Waterjet Cutting with Rivermark Waterjet</div></div>

  <div class="benefit-grid">
    <div class="benefit"><div class="benefit-icon"><svg width="30" height="30" viewBox="0 0 24 24"><path d="M12 3v18M3 12h18M6 6l12 12M18 6L6 18" stroke="#fff" stroke-width="1.8"/></svg></div><h3>Versatility</h3><p>Cuts metal, stone, glass, foam and more.</p></div>
    <div class="benefit"><div class="benefit-icon"><svg width="30" height="30" viewBox="0 0 24 24"><circle cx="12" cy="12" r="8" stroke="#fff" stroke-width="1.8" fill="none"/><circle cx="12" cy="12" r="2.5" fill="#fff"/><path d="M12 1v5M12 18v5M1 12h5M18 12h5" stroke="#fff" stroke-width="1.8"/></svg></div><h3>Precision</h3><p>Tight tolerances on every single part.</p></div>
    <div class="benefit"><div class="benefit-icon"><svg width="30" height="30" viewBox="0 0 24 24"><path d="M13 2L4 14h7l-1 8 9-12h-7z" fill="#fff"/></svg></div><h3>Speed</h3><p>Fast setup and quick turnaround times.</p></div>
    <div class="benefit"><div class="benefit-icon"><svg width="30" height="30" viewBox="0 0 24 24"><path d="M5 19C5 9 11 4 20 4c0 9-5 15-15 15zM5 19l8-8" stroke="#fff" stroke-width="1.8" fill="none"/></svg></div><h3>Eco Friendly</h3><p>No toxic fumes or hazardous waste.</p></div>
    <div class="benefit"><div class="benefit-icon"><svg width="30" height="30" viewBox="0 0 24 24"><path d="M12 2v20M3.5 7l17 10M20.5 7l-17 10" stroke="#fff" stroke-width="1.8"/></svg></div><h3>Cold Cutting Process</h3><p>No heat affected zone or warping.</p></div>
    <div class="benefit"><div class="benefit-icon"><svg width="30" height="30" viewBox="0 0 24 24"><path d="M3 8c3-3 6 3 9 0s6 3 9 0M3 14c3-3 6 3 9 0s6 3 9 0" stroke="#fff" stroke-width="1.8" fill="none"/></svg></div><h3>Smooth Edge Finish</h3><p>Clean edges with little secondary work.</p></div>
    <div class="benefit"><div class="benefit-icon"><svg width="30" height="30" viewBox="0 0 24 24"><rect x="4" y="4" width="16" height="16" stroke="#fff" stroke-width="1.8" fill="none"/><path d="M4 12h16M12 4v16" stroke="#fff" stroke-width="1.8"/></svg></div><h3>Material Savings</h3><p>Tight nesting keeps scrap to a minimum.</p></div>
    <div class="benefit"><div class="benefit-icon"><svg width="30" height="30" viewBox="0 0 24 24"><path d="M5 12l5 5 9-10" stroke="#fff" stroke-width="2.2" fill="none"/></svg></div><h3>Lower Cost</h3><p>Less tooling and finishing saves money.</p></div>
  </div>
  <div class="fold"></div>
</section>

<!-- Comparison / Materials spread -->
<section class="spread spread-compare">
  <h2 class="heading compare-title">Comparative<br><span class="accent">Cutting Technologies</span></h2>
  <table class="compare-table">
    <thead><tr><th></th><th>Waterjet</th><th>Laser</th><th>Plasma</th></tr></thead>
    <tbody>
      <tr><td>Materials</td><td>Nearly any material</td><td>Mostly metals and some plastics</td><td>Conductive metals only</td></tr>
      <tr><td>Thickness</td><td>Up to 8 inches</td><td>Up to 1 inch</td><td>Up to 2 inches</td></tr>
      <tr><td>Heat Zone</td><td>None</td><td>Small heat affected zone</td><td>Large heat affected zone</td></tr>
      <tr><td>Tolerance</td><td>+/- 0.003 inch</td><td>+/- 0.005 inch</td><td>+/- 0.020 inch</td></tr>
      <tr><td>Edge Quality</td><td>Smooth, satin finish</td><td>Good, slight burn marks</td><td>Rough, dross present</td></tr>
      <tr><td>Secondary Finishing</td><td>Rarely required</td><td>Sometimes required</td><td>Usually required</td></tr>
      <tr><td>Setup Time</td><td>Short</td><td>Short</td><td>Moderate</td></tr>
    </tbody>
  </table>

  <h2 class="heading materials-title">Materials<br><span class="accent">We Cut</span></h2>
  <div class="materials-grid">
    <div class="material"><h3>Metals</h3><p>Steel, stainless, aluminum, titanium, brass and copper cut cleanly at any thickness.</p></div>
    <div class="material"><h3>Composites</h3><p>Carbon fiber and fiberglass panels cut without fraying or layer separation.</p></div>
    <div class="material"><h3>Stone &amp; Tile</h3><p>Granite, marble and porcelain shaped for inlays, counters and detailed flooring.</p></div>
    <div class="material"><h3>Glass</h3><p>Flat and laminated glass cut with smooth edges and intricate profiles.</p></div>
    <div class="material"><h3>Foam</h3><p>Packaging and insulation foams trimmed precisely with no melted edges.</p></div>
    <div class="material"><h3>Plastic &amp; Rubber</h3><p>Gaskets, seals and plastic parts produced quickly with accurate shapes.</p></div>
    <div class="material"><h3>Wood</h3><p>Plywood and hardwood cut without burning for signs and cabinetry.</p></div>
    <div class="material"><h3>Ceramics</h3><p>Technical ceramics shaped carefully without cracking or thermal stress.</p></div>
  </div>
  <div class="fold"></div>
</section>

</body>
</html>
```